Kentucky residential recovery center needs a flyer design

We need a flyer design for a 16 bed male residential/inpatient recovery center based in Richmond, Kentucky. The facility provides short term (average 30 day) treatment to those struggling with substace abuse and addiction. The design should communicate trust, assurance, safety.
Our wesite provides more information https://brovalcare.org/treatment-services/residential-treatment/

Target Market(s)

Men (typically 30-50) struggling with substance addiction

```html
<!DOCTYPE html>
<html lang="en">
<head>
<meta charset="utf-8">
<title>Broval Care – Residential/Inpatient Treatment Flyer</title>
<link href="https://fonts.googleapis.com/css2?family=Poppins:wght@300;400;500;700;800;900&display=swap" rel="stylesheet">
<style>
  :root{
    --sky:#5eaeea;
    --sky-deep:#3f8fd6;
    --sky-pale:#9ccdf3;
    --navy:#0b0f78;
    --ink:#1b1b2a;
    --white:#ffffff;
    --backdrop:#e4e4e6;
  }
  *{box-sizing:border-box;margin:0;padding:0}
  html,body{width:1200px;height:1200px;overflow:hidden}
  body{background:var(--backdrop);font-family:'Poppins',sans-serif;color:var(--ink);position:relative}
  .flyer{
    position:absolute;left:187px;top:16px;width:825px;height:1168px;
    background:var(--white);overflow:hidden;
    transform:scale(.95);transform-origin:center center;
    box-shadow:0 6px 24px rgba(0,0,0,.12);
  }
  .hero{position:absolute;left:0;top:0;width:825px;height:560px}
  .brand{position:absolute;left:30px;top:48px;display:flex;align-items:center;gap:10px;
    color:var(--white);font-weight:700;font-size:22px}
  .brand-dot{width:26px;height:26px;border-radius:50%;background:var(--white)}
  .title{position:absolute;left:0;right:0;top:118px;text-align:center;color:var(--white);
    font-weight:800;font-size:46px;line-height:57px;letter-spacing:.5px}
  .badge{position:absolute;left:678px;top:508px;width:124px;height:124px;border-radius:50%;
    background:linear-gradient(150deg,#2b45c4,var(--navy));color:var(--white);
    display:flex;align-items:center;justify-content:center;text-align:center;
    font-weight:800;font-size:17px;line-height:20px;transform:rotate(14deg)}
  .issues-kicker{position:absolute;left:28px;top:570px;font-weight:400;font-size:29px;color:#111}
  .issues-title{position:absolute;left:28px;top:604px;font-weight:800;font-size:41px;color:var(--navy);letter-spacing:.2px}
  .issue{position:absolute;top:676px;width:200px;text-align:center;font-size:16px;line-height:22px;font-weight:400;text-transform:uppercase}
  .issue svg{display:block;margin:0 auto 14px}
  .services-bar{position:absolute;left:28px;top:815px;width:775px;height:50px;border-radius:12px;
    background:var(--navy);color:var(--white);font-weight:800;font-size:38px;line-height:50px;padding-left:14px}
  .service{position:absolute;font-size:18px;line-height:25px;font-weight:400;padding-left:18px}
  .service::before{content:"";position:absolute;left:0;top:8px;width:10px;height:10px;border-radius:50%;background:var(--sky)}
  .footer-band{position:absolute;left:0;top:1102px;width:825px;height:30px;background:var(--navy)}
  .contact-pill{position:absolute;left:30px;top:1092px;width:236px;height:50px;border-radius:10px;
    background:var(--sky);color:var(--white);font-weight:700;font-size:19px;line-height:50px;text-align:center;letter-spacing:.4px}
  .footer-item{position:absolute;top:1104px;color:var(--white);font-size:16px;line-height:26px;display:flex;align-items:center;gap:8px}
</style>
</head>
<body>
<main class="flyer">
  <svg class="hero" viewBox="0 0 825 560" width="825" height="560">
    <defs>
      <linearGradient id="roomTint" x1="0" y1="0" x2="1" y2="1">
        <stop offset="0" stop-color="#6cb6ee"/>
        <stop offset=".6" stop-color="#4c9ee0"/>
        <stop offset="1" stop-color="#3b86cc"/>
      </linearGradient>
      <linearGradient id="meetingRoom" x1="0" y1="0" x2="0" y2="1">
        <stop offset="0" stop-color="#e6e2dc"/><stop offset=".55" stop-color="#8c8a88"/><stop offset="1" stop-color="#3a3532"/>
      </linearGradient>
      <linearGradient id="bedroom" x1="0" y1="0" x2="0" y2="1">
        <stop offset="0" stop-color="#d9c7a4"/><stop offset=".55" stop-color="#8a7a62"/><stop offset="1" stop-color="#5a4a3a"/>
      </linearGradient>
      <linearGradient id="lounge" x1="0" y1="0" x2="0" y2="1">
        <stop offset="0" stop-color="#eceae6"/><stop offset=".6" stop-color="#8a8078"/><stop offset="1" stop-color="#6a4c44"/>
      </linearGradient>
    </defs>
    <rect role="img" aria-label="Blue-tinted photo of a residential bedroom with bunk beds" width="825" height="560" fill="url(#roomTint)"/>
    <path d="M0 500 C 200 420, 520 430, 825 380 L825 560 L0 560 Z" fill="var(--navy)"/>
    <path d="M0 534 C 220 448, 540 452, 825 414 L825 560 L0 560 Z" fill="var(--white)"/>
    <g role="img" aria-label="Photo of a conference room with a dark table and office chairs">
      <circle cx="184" cy="394" r="106" fill="var(--sky)"/>
      <circle cx="184" cy="394" r="98" fill="url(#meetingRoom)"/>
    </g>
    <g role="img" aria-label="Photo of a bedroom with a wooden bunk bed and a sofa">
      <circle cx="641" cy="394" r="106" fill="var(--sky)"/>
      <circle cx="641" cy="394" r="98" fill="url(#lounge)"/>
    </g>
    <g role="img" aria-label="Photo of a lounge with a leather sofa, rug and television">
      <circle cx="419" cy="392" r="150" fill="var(--navy)"/>
      <circle cx="419" cy="392" r="140" fill="url(#bedroom)"/>
    </g>
  </svg>

  <div class="brand"><span class="brand-dot"></span>Broval Care</div>
  <h1 class="title">RESIDENTIAL/INPATIENT<br>TREATMENT</h1>
  <div class="badge">SPACES<br>AVAILABLE!</div>

  <p class="issues-kicker">Problems we can help with</p>
  <h2 class="issues-title">What Issues can be Treated?</h2>

  <div class="issue" style="left:-13px">
    <svg width="58" height="58" viewBox="0 0 58 58"><circle cx="29" cy="29" r="27" fill="none" stroke="var(--sky)" stroke-width="2"/>
      <path d="M26 12h6v8l4 5v20h-14V25l4-5z" fill="var(--sky)"/></svg>
    Alcoholism</div>
  <div class="issue" style="left:207px">
    <svg width="58" height="58" viewBox="0 0 58 58"><circle cx="29" cy="29" r="27" fill="none" stroke="var(--sky)" stroke-width="2"/>
      <g transform="rotate(45 29 29)" fill="var(--sky)"><rect x="24" y="16" width="10" height="20" rx="2"/><rect x="21" y="14" width="16" height="3"/><rect x="28" y="8" width="2" height="7"/><rect x="28" y="36" width="2" height="10"/></g></svg>
    Drug Addiction</div>
  <div class="issue" style="left:431px">
    <svg width="58" height="58" viewBox="0 0 58 58"><circle cx="29" cy="29" r="27" fill="none" stroke="var(--sky)" stroke-width="2"/>
      <g transform="rotate(-45 29 29)"><rect x="14" y="21" width="30" height="16" rx="8" fill="var(--sky)"/><rect x="29" y="23" width="13" height="12" rx="6" fill="var(--white)"/></g></svg>
    Medication<br>Addiction</div>
  <div class="issue" style="left:648px">
    <svg width="58" height="58" viewBox="0 0 58 58"><circle cx="29" cy="29" r="27" fill="none" stroke="var(--sky)" stroke-width="2"/>
      <circle cx="29" cy="26" r="12" fill="var(--sky)"/><rect x="23" y="34" width="10" height="11" fill="var(--sky)"/>
      <path d="M22 24h14M24 29h10M29 16v18" stroke="var(--white)" stroke-width="1.6" fill="none"/></svg>
    Behavioral<br>Health</div>

  <h2 class="services-bar">Our Services</h2>
  <p class="service" style="left:30px;top:897px">Outpatient</p>
  <p class="service" style="left:277px;top:895px">Intensive Outpatient</p>
  <p class="service" style="left:582px;top:897px">Residential</p>
  <p class="service" style="left:30px;top:955px">Targeted Case<br>Management</p>
  <p class="service" style="left:277px;top:955px">Medicated Assisted<br>Treatment (‘MAT’)</p>
  <p class="service" style="left:582px;top:957px">Individual and Group<br>Therapy</p>
  <p class="service" style="left:30px;top:1034px">Peer Support</p>
  <p class="service" style="left:277px;top:1034px">Physician Appointments</p>
  <p class="service" style="left:582px;top:1034px">Telemedicine</p>

  <div class="footer-band"></div>
  <div class="contact-pill">CONTACT US NOW</div>
  <p class="footer-item" style="left:362px">
    <svg width="20" height="20" viewBox="0 0 20 20"><circle cx="10" cy="10" r="10" fill="var(--white)"/>
      <path d="M6.5 5.5l2 .2.8 2.3-1.2 1a6 6 0 0 0 2.9 2.9l1-1.2 2.3.8.2 2a1.2 1.2 0 0 1-1.3 1A8.5 8.5 0 0 1 5.5 6.8a1.2 1.2 0 0 1 1-1.3z" fill="var(--navy)"/></svg>
    859-555-0148</p>
  <p class="footer-item" style="left:592px">
    <svg width="20" height="20" viewBox="0 0 20 20"><circle cx="10" cy="10" r="10" fill="var(--white)"/>
      <g fill="none" stroke="var(--navy)" stroke-width="1.2"><circle cx="10" cy="10" r="6"/><ellipse cx="10" cy="10" rx="2.6" ry="6"/><path d="M4 10h12"/></g></svg>
    www.brovalcare.org</p>
</main>
</body>
</html>
```